July 4th Postcard to existing clients

5x7 postcard wishing our clients happy 4th of July. Card should read on the back "Thank You For Being A Valued Client!. Stay Safe And Enjoy Your Independence Day Celebrations!"

Patriotic theme with fireworks is ideal. We are a law firm so should still have a feel of professionalism while still being fun since it is for a fun holiday.

```html
<!DOCTYPE html>
<html lang="en">
<head>
<meta charset="utf-8">
<title>Marlow Law – Independence Day Postcard</title>
<link href="https://fonts.googleapis.com/css2?family=Great+Vibes&family=Cinzel:wght@700&family=Fira+Sans:wght@300;400;600;700&display=swap" rel="stylesheet">
<style>
  :root {
    --backdrop: #d9dadd;
    --night: #07070d;
    --night-deep: #0d1630;
    --night-blue: #1a4a78;
    --ink-white: #ffffff;
    --holiday-red: #e02424;
    --brand-slate: #7d8093;
    --panel-lilac: #9094b6;
    --panel-text: #ffffff;
    --body-grey: #9c9fb5;
    --stamp-grey: #8a8a8a;
    --rule-grey: #9a9a9a;
    --card-white: #ffffff;
  }
  * { box-sizing: border-box; margin: 0; padding: 0; }
  html, body { width: 952px; height: 1200px; overflow: hidden; }
  body { background: var(--backdrop); position: relative; font-family: "Fira Sans", sans-serif; }

  .postcard {
    position: absolute; left: 156px; width: 640px; height: 457px; overflow: hidden;
    box-shadow: 0 6px 18px rgba(0,0,0,.25);
  }
  .postcard--front { top: 96px; background: linear-gradient(180deg, var(--night) 0%, var(--night) 55%, var(--night-deep) 82%, var(--night-blue) 100%); }
  .postcard--back { top: 633px; background: var(--card-white); }

  .fireworks-photo {
    position: absolute; left: 300px; top: 10px; width: 330px; height: 447px;
    background:
      radial-gradient(circle at 50% 52%, rgba(255,190,140,.9) 0, rgba(240,110,60,.65) 8%, transparent 22%),
      radial-gradient(circle at 52% 38%, rgba(255,220,200,.85) 0, rgba(150,110,230,.7) 12%, rgba(90,70,200,.35) 30%, transparent 45%),
      radial-gradient(circle at 50% 56%, rgba(230,100,50,.55) 0, transparent 30%);
  }

  .greeting-title {
    position: absolute; left: 10px; top: 52px; width: 310px; text-align: center;
    white-space: nowrap;
    font-family: "Great Vibes", cursive; font-weight: 400; font-size: 62px; line-height: 1; color: var(--ink-white);
  }
  .greeting-rule { position: absolute; left: 68px; top: 138px; width: 200px; height: 1px; background: rgba(255,255,255,.5); }
  .greeting-sub {
    position: absolute; left: 20px; top: 144px; width: 300px; text-align: center; white-space: nowrap;
    font-family: "Cinzel", serif; font-weight: 700; font-size: 12.5px; color: var(--ink-white); letter-spacing: .3px;
  }
  .holiday-wish {
    position: absolute; left: 20px; top: 222px; width: 300px; text-align: center;
    font-family: "Cinzel", serif; font-weight: 700; color: var(--holiday-red); line-height: 1.2;
  }
  .holiday-wish .small { font-size: 15px; display: block; }
  .holiday-wish .large { font-size: 19px; display: block; }

  .brand { display: flex; align-items: center; gap: 9px; font-family: "Fira Sans", sans-serif; font-weight: 300; letter-spacing: 1px; white-space: nowrap; }
  .brand-mark { width: 16px; height: 16px; }
  .postcard--front .brand { position: absolute; left: 76px; top: 390px; color: #d9dae4; font-size: 22px; }
  .postcard--front .brand-mark { background: #b9bbd0; }
  .postcard--back .brand { position: absolute; left: 64px; top: 74px; color: var(--brand-slate); font-size: 25px; }
  .postcard--back .brand-mark { background: var(--panel-lilac); }

  .about-panel {
    position: absolute; left: 0; top: 131px; width: 320px; height: 190px;
    background: var(--panel-lilac); color: var(--panel-text); padding: 10px 16px 0 16px;
  }
  .about-panel h2 { font-size: 12.5px; font-weight: 600; margin-bottom: 5px; letter-spacing: .2px; }
  .about-panel p { font-size: 9.2px; line-height: 1.32; font-weight: 300; margin-bottom: 7px; }

  .contact { position: absolute; left: 16px; top: 354px; color: var(--body-grey); font-size: 9.6px; line-height: 1.35; }
  .toll-free { position: absolute; left: 16px; top: 388px; color: var(--body-grey); font-size: 20px; font-weight: 600; }

  .stamp-box { position: absolute; left: 540px; top: 54px; width: 66px; height: 66px; background: var(--stamp-grey); }
  .address-line { position: absolute; left: 344px; width: 262px; height: 1px; background: var(--rule-grey); }
  .address-line--1 { top: 296px; }
  .address-line--2 { top: 343px; }
  .address-line--3 { top: 389px; }
</style>
</head>
<body>

<section class="postcard postcard--front" aria-label="Postcard front">
  <div class="fireworks-photo" role="img" aria-label="Photo of purple and orange fireworks bursting in the night sky"></div>
  <h1 class="greeting-title">Thank You</h1>
  <div class="greeting-rule"></div>
  <p class="greeting-sub">For Being A Valued Client!</p>
  <p class="holiday-wish">
    <span class="small">Stay Safe And Enjoy Your</span>
    <span class="large">Independence Day</span>
    <span class="large">Celebrations!</span>
  </p>
  <div class="brand"><span class="brand-mark"></span><span>MARLOW LAW</span></div>
</section>

<section class="postcard postcard--back" aria-label="Postcard back">
  <div class="brand"><span class="brand-mark"></span><span>MARLOW LAW</span></div>
  <div class="about-panel">
    <h2>YOUR INJURY ATTORNEY IN FAIRVIEW, MO</h2>
    <p>When you've suffered injuries or the loss of a loved one because of someone else's carelessness, contact Marlow Law to set up your FREE consultation.</p>
    <p>For more than 30 years, attorney Dana Marlow has helped people just like you by holding responsible parties accountable for their actions in personal injury cases.</p>
    <p>All you have to do is fill out our convenient on-line form or just give us a call at 555-210-4470. Dana looks forward to discussing the details of your case - at no cost to you.</p>
  </div>
  <p class="contact">1820 North Alder Avenue, Fairview, Missouri 65900<br>Telephone: (555) 210-4470 | Fax: (555) 210-4471</p>
  <p class="toll-free">Toll Free: 1-800-555-0142</p>
  <div class="stamp-box"></div>
  <div class="address-line address-line--1"></div>
  <div class="address-line address-line--2"></div>
  <div class="address-line address-line--3"></div>
</section>

</body>
</html>
```